Land Buying Company Needs Letterhead for Direct Mail Marketing to Land Owners

We are looking for a professional letterhead that we will be including in our direct mail marketing. We will be sending this to land owners who may be interested in selling or purchasing land.

The letterhead needs to be editable. Headers and footers would look nice, but we are open. We would want it to include our address, website, phone, and email info. For right now the address to use for design purposes would the following:

Address: 415 Bramwell Avenue #600
Dallas, TX 75219
Website - www.quillridgeacres.example
Email - info@quillridgeacres.example
Phone - 866-402-ACRE

I have attached our logo zip file that we just had done on Pixel Guild. Let me know what questions you have, and thank you.

```html
<!DOCTYPE html>
<html lang="en">
<head>
<meta charset="utf-8">
<title>Quill Ridge Acres — Letterhead</title>
<link rel="stylesheet" href="https://fonts.googleapis.com/css2?family=Montserrat:wght@600&family=Open+Sans:wght@300&display=swap">
<style>
  :root {
    --green-deep: #7aa446;
    --green-mid: #a9d46a;
    --green-pale: #cfe6ad;
    --grey-light: #eef0ef;
    --grey-mid: #e2e2e2;
    --grey-dark: #d6d6d6;
    --text-grey: #6a6a6a;
    --icon-green: #7aa446;
    --paper: #ffffff;
  }
  html, body {
    margin: 0;
    padding: 0;
    overflow: hidden;
    background: var(--paper);
  }
  .letterhead {
    position: relative;
    width: 927px;
    height: 1200px;
    overflow: hidden;
    background: var(--paper);
  }
  .decor {
    position: absolute;
    inset: 0;
    width: 927px;
    height: 1200px;
  }
  .brand {
    position: absolute;
    left: 25px;
    top: 43px;
    display: flex;
    align-items: center;
    gap: 14px;
  }
  .brand-mark {
    width: 66px;
    height: 66px;
    border-radius: 50%;
    background: var(--paper);
    flex: none;
  }
  .brand-name {
    font-family: "Montserrat", sans-serif;
    font-weight: 600;
    font-size: 24px;
    line-height: 1.12;
    letter-spacing: 3px;
    color: var(--paper);
    margin: 0;
    text-transform: uppercase;
    white-space: nowrap;
  }
  .brand-name-line {
    display: block;
  }
  .contact {
    position: absolute;
    left: 26px;
    top: 1088px;
    margin: 0;
    padding: 0;
    list-style: none;
    font-family: "Open Sans", sans-serif;
    font-weight: 300;
    font-size: 12.5px;
    color: var(--text-grey);
  }
  .contact-item {
    display: flex;
    align-items: center;
    gap: 5px;
    height: 18px;
    margin-bottom: 5px;
  }
  .contact-icon {
    width: 18px;
    height: 18px;
    flex: none;
  }
</style>
</head>
<body>
<main class="letterhead">
  <svg class="decor" viewBox="0 0 927 1200" aria-hidden="true">
    <g class="header-circles">
      <circle cx="368" cy="-220" r="267" fill="var(--green-pale)" opacity="0.7"/>
      <circle cx="231" cy="-95" r="236" fill="var(--green-mid)" opacity="0.75"/>
      <circle cx="27" cy="-55" r="235" fill="var(--green-deep)" opacity="0.85"/>
    </g>
    <g class="footer-circles">
      <circle cx="696" cy="1335" r="275" fill="var(--grey-light)" opacity="0.9"/>
      <circle cx="902" cy="1268" r="248" fill="var(--grey-dark)" opacity="0.85"/>
      <circle cx="555" cy="1483" r="330" fill="var(--grey-mid)" opacity="0.8"/>
    </g>
  </svg>

  <header class="brand">
    <div class="brand-mark"></div>
    <h1 class="brand-name">
      <span class="brand-name-line">Quill Ridge</span>
      <span class="brand-name-line">Acres</span>
    </h1>
  </header>

  <ul class="contact">
    <li class="contact-item">
      <svg class="contact-icon" viewBox="0 0 18 18"><circle cx="9" cy="9" r="9" fill="var(--icon-green)"/><path d="M9 3.8a3.3 3.3 0 0 0-3.3 3.3c0 2.4 3.3 6.2 3.3 6.2s3.3-3.8 3.3-6.2A3.3 3.3 0 0 0 9 3.8z" fill="#fff"/><circle cx="9" cy="7.1" r="1.3" fill="var(--icon-green)"/></svg>
      <span>415 Bramwell Avenue #600 Dallas, TX 75219</span>
    </li>
    <li class="contact-item">
      <svg class="contact-icon" viewBox="0 0 18 18"><circle cx="9" cy="9" r="9" fill="var(--icon-green)"/><path d="M6 4.5l1.6 2.4-1 1c.6 1.3 1.5 2.2 2.8 2.8l1-1 2.4 1.6-.8 1.6c-3.6-.3-6.4-3.1-6.7-6.7z" fill="#fff"/></svg>
      <span>866-402-ACRE</span>
    </li>
    <li class="contact-item">
      <svg class="contact-icon" viewBox="0 0 18 18"><circle cx="9" cy="9" r="9" fill="var(--icon-green)"/><rect x="4.5" y="5" width="9" height="8" fill="#fff"/><rect x="4.5" y="5" width="9" height="1.6" fill="#dfe9d0"/><rect x="6" y="8" width="2.5" height="3.5" fill="#cfdcbc"/></svg>
      <span>www.quillridgeacres.example</span>
    </li>
    <li class="contact-item">
      <svg class="contact-icon" viewBox="0 0 18 18"><circle cx="9" cy="9" r="9" fill="var(--icon-green)"/><rect x="4.5" y="5.8" width="9" height="6.4" fill="#fff"/><path d="M4.5 5.8L9 9.4l4.5-3.6M4.5 12.2L7.6 8.9M13.5 12.2L10.4 8.9" fill="none" stroke="var(--icon-green)" stroke-width="0.7"/></svg>
      <span>info@quillridgeacres.example</span>
    </li>
  </ul>
</main>
</body>
</html>
```